Landscape Contractor in need of New Web Design

HELP.. Please Help!!!!. Our current website is old, outdated, ugly... and well nothing like us.... so we are looking for someone to help build a new website that fits our company direction. We are a landscape company with multiple locations in order to meet the needs of our clients and their projects throughout the midwest. When most people think of landscaping, they think of mowing grandmas yard, but that is NOT even remotely close to what we do. We are 100% a commercial landscape company meaning we complete landscape and irrigation services for large scale commercial projects. We are looking for a website to showcase our commercial talents and awesome team of people.
Updates

Address of current website is www.brookvaleyardworks.com

```html
<!DOCTYPE html>
<html lang="en">
<head>
<meta charset="utf-8">
<title>Brookvale Yardworks</title>
<link href="https://fonts.googleapis.com/css2?family=Ubuntu:wght@400;500;700&display=swap" rel="stylesheet">
<style>
:root{
  --lime:#8cc63f;
  --lime-dark:#6fa52a;
  --forest:#1f4a14;
  --forest-deep:#173a0f;
  --mint:#edf7df;
  --ink:#2b2b2b;
  --muted:#6b6b6b;
  --line:#e2e2e2;
  --footer:#1d1f1c;
  --white:#ffffff;
}
*{box-sizing:border-box;margin:0;padding:0}
html,body{width:1200px;height:4920px;overflow:hidden}
body{font-family:'Ubuntu',sans-serif;color:var(--ink);background:var(--white);position:relative}
.abs{position:absolute}
.btn{position:absolute;background:var(--lime);color:var(--forest-deep);font-weight:700;font-size:14px;letter-spacing:1px;border-radius:24px;display:flex;align-items:center;justify-content:center;text-transform:uppercase}
.center{text-align:center}
.eyebrow{color:var(--lime-dark);font-size:22px;font-weight:500}
.h2{font-size:50px;font-weight:700;color:var(--ink)}
.lead{font-size:16px;line-height:26px;color:var(--muted)}
.photo{position:absolute;overflow:hidden}

/* header */
.site-header{position:absolute;left:0;top:0;width:1200px;height:156px;background:var(--white)}
.brand{position:absolute;left:28px;top:22px;display:flex;align-items:center;gap:12px}
.brand-dot{width:22px;height:22px;border-radius:50%;background:var(--lime)}
.brand-name{font-size:30px;font-weight:700;color:var(--forest)}
.topbar{position:absolute;right:30px;top:22px;display:flex;gap:26px;font-size:16px;font-weight:700;color:var(--forest);align-items:center}
.topbar .pay{background:var(--mint);padding:8px 18px;border-radius:20px}
.nav{position:absolute;left:360px;top:96px;display:flex;gap:34px;font-size:17px;font-weight:500;color:var(--ink)}
.nav .caret{font-size:11px;color:var(--lime-dark)}

/* hero */
.hero{position:absolute;left:0;top:156px;width:1200px;height:604px;background:linear-gradient(90deg,#3a6a2c 0%,#5f8d3c 40%,#9a7b6a 70%,#c96a8a 100%)}
.hero-title{position:absolute;left:80px;top:190px;font-size:62px;line-height:68px;font-weight:700;color:var(--white)}
.hero-sub{position:absolute;left:80px;top:420px;font-size:28px;line-height:34px;font-weight:500;color:var(--white)}
.dots{position:absolute;display:flex;gap:14px}
.dots span{width:40px;height:5px;background:#d8d8d8;border-radius:3px}
.dots span.on{background:var(--lime)}

/* welcome features */
.feature{position:absolute;width:330px;text-align:center}
.feature .ico{width:56px;height:56px;margin:0 auto 12px;border-radius:50%;background:var(--mint);border:2px solid var(--lime)}
.feature h3{font-size:22px;font-weight:700;margin-bottom:10px}
.feature p{font-size:14px;line-height:22px;color:var(--muted)}

/* services */
.services-band{position:absolute;left:0;top:1848px;width:1200px;height:792px;background:var(--mint)}
.service{position:absolute;width:240px;text-align:center}
.service .ico{width:90px;height:90px;margin:0 auto 20px;border-radius:50%;background:#cfe8ad}
.service h4{font-size:22px;font-weight:700}

/* projects */
.project-label{position:absolute;width:240px;text-align:center;font-size:24px;font-weight:700}

/* estimate */
.estimate-band{position:absolute;left:0;top:3480px;width:1200px;height:1100px;background:var(--forest)}
.card{position:absolute;left:80px;top:3228px;width:1040px;height:592px;background:var(--white);border-radius:14px;overflow:hidden;box-shadow:0 10px 30px rgba(0,0,0,.15)}
.field{position:absolute;left:60px;width:420px;height:52px;border:1px solid var(--line);border-radius:6px;font-size:13px;font-weight:700;color:var(--ink);padding:18px 18px;letter-spacing:.5px}

/* testimonials */
.quote{position:absolute;top:4080px;width:492px;height:192px;border:1px solid rgba(255,255,255,.35);border-radius:8px;padding:30px 110px 30px 36px;color:var(--white);font-size:15px;line-height:24px}
.quote .mark{position:absolute;right:34px;top:28px;font-size:90px;line-height:70px;color:var(--lime);font-weight:700}
.person{position:absolute;top:4316px;display:flex;align-items:center;gap:18px;color:var(--white)}
.avatar{width:70px;height:70px;border-radius:50%;background:#b8c4b0}
.person b{display:block;font-size:16px}
.person span{font-size:13px;color:#c7d6bd}

/* footer */
.site-footer{position:absolute;left:0;top:4580px;width:1200px;height:340px;background:var(--footer);color:#d8d8d8;font-size:15px}
.f-row{position:absolute;display:flex;align-items:center;gap:12px}
.f-row svg{flex:none}
.footer-brand{position:absolute;left:400px;top:66px;width:400px;display:flex;align-items:center;justify-content:center;gap:12px}
.footer-brand .brand-dot{width:18px;height:18px}
.footer-brand .brand-name{font-size:28px;color:var(--white)}
</style>
</head>
<body>

<header class="site-header">
  <div class="brand"><div class="brand-dot"></div><div class="brand-name">Brookvale Yardworks</div></div>
  <div class="topbar">
    <span class="pay">MAKE A PAYMENT</span>
    <span>(555) 210-4480 &nbsp;|&nbsp; (555) 318-9026</span>
  </div>
  <nav class="nav">
    <span>Home</span><span>Divisions <span class="caret">▼</span></span><span>Services <span class="caret">▼</span></span><span>About Us <span class="caret">▼</span></span><span>Gallery</span><span>Contact</span>
  </nav>
  <div class="btn" style="left:1010px;top:86px;width:160px;height:44px">Get a Quote</div>
</header>

<section class="hero" role="img" aria-label="Lush green lawn beside a house with colourful flower beds and shrubs">
  <h1 class="hero-title">Landscape<br>Maintenance<br>Service</h1>
  <p class="hero-sub">With the goal of crafting<br>A purposefull landscape</p>
  <div class="btn" style="left:80px;top:504px;width:140px;height:42px;background:var(--white)">About Us</div>
  <div class="dots" style="left:544px;top:540px"><span class="on"></span><span></span><span></span></div>
</section>

<section class="welcome">
  <p class="abs eyebrow center" style="left:0;top:836px;width:1200px">Welcome</p>
  <h2 class="abs h2 center" style="left:0;top:870px;width:1200px">We Are Brookvale Yardworks</h2>
  <p class="abs lead center" style="left:300px;top:940px;width:600px">Brookvale Yardworks strives to set the standard for the highest quality lawn and landscape products and services and to exceed our customer's expectations every time.</p>

  <div class="feature" style="left:60px;top:1030px"><div class="ico" role="img" aria-label="Company icon"></div><h3>Specialized Company</h3><p>Brookvale Yardworks strives to set the standard for the highest quality lawn and landscape products and services for every client.</p></div>
  <div class="feature" style="left:60px;top:1260px"><div class="ico" role="img" aria-label="Handshake icon"></div><h3>Dependable Services</h3><p>Communication is highly valued at our office. From start to finish our clients will be kept up to date on their project.</p></div>
  <div class="feature" style="left:60px;top:1490px"><div class="ico" role="img" aria-label="Consultation icon"></div><h3>Free Consultations</h3><p>Call our office to set up a time to meet with one of our qualified professionals who will walk your property and share ideas.</p></div>

  <div class="feature" style="left:810px;top:1030px"><div class="ico" role="img" aria-label="Certificate icon"></div><h3>Licensed &amp; Insured</h3><p>Rest assured knowing that we are fully licensed and insured and have a superior safety rating.</p></div>
  <div class="feature" style="left:810px;top:1260px"><div class="ico" role="img" aria-label="Calendar icon"></div><h3>Day Scheduling</h3><p>Contact our office today to schedule an appointment that meets your needs.</p></div>
  <div class="feature" style="left:810px;top:1490px"><div class="ico" role="img" aria-label="Award icon"></div><h3>Reputable Company</h3><p>With 15 years of experience in the landscaping construction business, we have built a reputation for superior projects.</p></div>

  <div class="photo" style="left:510px;top:1040px;width:180px;height:180px;border-radius:50%;background:linear-gradient(135deg,#6f9a4a,#3e6b2a)" role="img" aria-label="Shrubs and lawn beside a building"></div>
  <div class="photo" style="left:440px;top:1200px;width:320px;height:320px;border-radius:50%;background:linear-gradient(160deg,#7aa85a,#4b7a35 60%,#2e4f22)" role="img" aria-label="Crew member trimming grass with a string trimmer"></div>
  <div class="photo" style="left:510px;top:1500px;width:180px;height:180px;border-radius:50%;background:linear-gradient(135deg,#c47a8a,#5f8b3e)" role="img" aria-label="Planted flower bed with young shrubs"></div>
</section>

<section class="services-band">
  <h2 class="abs h2 center" style="left:0;top:176px;width:1200px">What We Do</h2>
  <p class="abs lead center" style="left:250px;top:248px;width:700px">Our company's dedication to innovative design projects created some of the most distinguished landscape projects throughout Kansas, Missouri, and Oklahoma</p>
  <div class="service" style="left:72px;top:310px"><div class="ico" role="img" aria-label="Mowing icon"></div><h4>Maintenance</h4></div>
  <div class="service" style="left:352px;top:310px"><div class="ico" role="img" aria-label="Fertilizer icon"></div><h4>Chemical Applications<br>&amp; Fertilization</h4></div>
  <div class="service" style="left:616px;top:310px"><div class="ico" role="img" aria-label="Turf roll icon"></div><h4>Turf Management</h4></div>
  <div class="service" style="left:872px;top:310px"><div class="ico" role="img" aria-label="Plant icon"></div><h4>Hardscaping</h4></div>
  <div class="service" style="left:360px;top:500px"><div class="ico" role="img" aria-label="Sprinkler icon"></div><h4>Irrigation</h4></div>
  <div class="service" style="left:640px;top:500px"><div class="ico" role="img" aria-label="Planting icon"></div><h4>Landscaping</h4></div>
  <div class="btn" style="left:520px;top:700px;width:160px;height:42px">Join Services</div>
</section>

<section class="projects">
  <h2 class="abs h2 center" style="left:0;top:2736px;width:1200px">Featured Projects</h2>
  <p class="abs lead center" style="left:0;top:2810px;width:1200px">Brookvale Yardworks is a full service lawn and landscape contractor providing design, installation, and maintenance services.</p>
  <div class="photo" style="left:88px;top:2856px;width:240px;height:170px;background:linear-gradient(180deg,#3f6b2c,#6fa040)" role="img" aria-label="Striped sports field with mower"></div>
  <div class="photo" style="left:352px;top:2856px;width:240px;height:170px;background:linear-gradient(180deg,#a9b8c4,#6f8a50)" role="img" aria-label="Government building with landscaped grounds"></div>
  <div class="photo" style="left:612px;top:2856px;width:240px;height:170px;background:linear-gradient(180deg,#4d7a33,#9cbf5a)" role="img" aria-label="Commercial planting beds"></div>
  <div class="photo" style="left:876px;top:2856px;width:240px;height:170px;background:linear-gradient(180deg,#b7a594,#5e8a3a)" role="img" aria-label="Residential home with flower beds"></div>
  <div class="project-label" style="left:88px;top:3046px">Sports Fields</div>
  <div class="project-label" style="left:352px;top:3046px">Government</div>
  <div class="project-label" style="left:612px;top:3046px">Commercial</div>
  <div class="project-label" style="left:876px;top:3046px">Residencial</div>
  <div class="btn" style="left:520px;top:3124px;width:160px;height:42px">View Gallery</div>
</section>

<div class="estimate-band"></div>
<section class="card">
  <p class="abs eyebrow" style="left:60px;top:60px;font-size:20px">Need Any Consultations</p>
  <h2 class="abs" style="left:60px;top:96px;font-size:40px;font-weight:700;color:var(--forest)">Join Free Estimate</h2>
  <div class="field" style="top:180px">YOUR NAME</div>
  <div class="field" style="top:252px">YOUR EMAIL</div>
  <div class="field" style="top:324px">SNOW REMOVAL <span style="float:right;color:var(--lime-dark)">▼</span></div>
  <div class="field" style="top:396px;height:110px">YOUR MESSAGE</div>
  <div class="btn" style="left:60px;top:530px;width:150px;height:40px">Submit</div>
  <svg class="abs" style="left:560px;top:0" width="480" height="592" viewBox="0 0 480 592" aria-hidden="true">
    <polygon points="200,0 480,0 480,592 380,592" fill="var(--lime-dark)"/>
  </svg>
  <div class="photo" style="left:560px;top:44px;width:340px;height:488px;background:linear-gradient(160deg,#6b9a4a,#a7c06a 40%,#d98aa0 75%,#f0c8d2)" role="img" aria-label="Garden bed with blooming hibiscus and trees"></div>
</section>

<section class="testimonials">
  <p class="abs center" style="left:0;top:3956px;width:1200px;color:var(--lime);font-size:18px;font-weight:700;letter-spacing:2px">TESTIMONIALS</p>
  <h2 class="abs center" style="left:0;top:3990px;width:1200px;color:var(--white);font-size:44px;font-weight:700">What our client's Say</h2>
  <div class="quote" style="left:88px">I have been working with Brookvale Yardworks for several years. As a building development firm I understand the importance of landscaping. They have provided expert consultation on all projects.<span class="mark">”</span></div>
  <div class="quote" style="left:628px">I have been working with Brookvale Yardworks for several years. As a building development firm I understand the importance of landscaping. They have provided expert consultation on all projects.<span class="mark">”</span></div>
  <div class="person" style="left:120px"><div class="avatar" role="img" aria-label="Client portrait"></div><div><b>DANIEL R HOLLIS</b><span>Client Operations &amp; Maintenance, Ridgefield Campus</span></div></div>
  <div class="person" style="left:660px"><div class="avatar" role="img" aria-label="Client portrait"></div><div><b>MARCUS T LINDEN</b><span>Linden Build Group</span></div></div>
  <div class="dots" style="left:544px;top:4470px"><span class="on"></span><span></span><span></span></div>
</section>

<footer class="site-footer">
  <div class="f-row" style="left:80px;top:50px"><svg width="16" height="20" viewBox="0 0 16 20"><path d="M8 0C3.6 0 0 3.5 0 7.8 0 13.5 8 20 8 20s8-6.5 8-12.2C16 3.5 12.4 0 8 0zm0 11a3 3 0 110-6 3 3 0 010 6z" fill="var(--lime)"/></svg><span>1480 Orchard Lane<br>Fairhaven, KS 66210</span></div>
  <div class="f-row" style="left:80px;top:118px"><svg width="18" height="18" viewBox="0 0 24 24"><path d="M6.6 10.8a15 15 0 006.6 6.6l2.2-2.2a1 1 0 011-.25 11.4 11.4 0 003.6.57 1 1 0 011 1V20a1 1 0 01-1 1A17 17 0 013 4a1 1 0 011-1h3.5a1 1 0 011 1c0 1.25.2 2.45.57 3.57a1 1 0 01-.25 1z" fill="var(--lime)"/></svg><span>1 (555) 210-4480</span></div>
  <div class="f-row" style="left:80px;top:164px"><svg width="18" height="14" viewBox="0 0 18 14"><rect width="18" height="14" rx="2" fill="var(--lime)"/><path d="M1 2l8 6 8-6" stroke="#1d1f1c" stroke-width="1.6" fill="none"/></svg><span>hello@brookvaleyardworks.com</span></div>

  <div class="footer-brand"><div class="brand-dot"></div><div class="brand-name">Brookvale Yardworks</div></div>
  <div class="abs" style="left:546px;top:150px;display:flex;gap:22px">
    <span style="width:20px;height:20px;border-radius:50%;background:#d8d8d8"></span>
    <span style="width:20px;height:20px;border-radius:50%;background:#d8d8d8"></span>
    <span style="width:20px;height:20px;border-radius:50%;background:#d8d8d8"></span>
  </div>

  <div class="f-row" style="left:900px;top:50px"><svg width="16" height="20" viewBox="0 0 16 20"><path d="M8 0C3.6 0 0 3.5 0 7.8 0 13.5 8 20 8 20s8-6.5 8-12.2C16 3.5 12.4 0 8 0zm0 11a3 3 0 110-6 3 3 0 010 6z" fill="var(--lime)"/></svg><span>902 Millstone Road<br>Cedar Bluff, KS 66441</span></div>
  <div class="f-row" style="left:900px;top:118px"><svg width="18" height="18" viewBox="0 0 24 24"><path d="M6.6 10.8a15 15 0 006.6 6.6l2.2-2.2a1 1 0 011-.25 11.4 11.4 0 003.6.57 1 1 0 011 1V20a1 1 0 01-1 1A17 17 0 013 4a1 1 0 011-1h3.5a1 1 0 011 1c0 1.25.2 2.45.57 3.57a1 1 0 01-.25 1z" fill="var(--lime)"/></svg><span>1 (555) 318-9026</span></div>
  <div class="f-row" style="left:900px;top:164px"><svg width="18" height="14" viewBox="0 0 18 14"><rect width="18" height="14" rx="2" fill="var(--lime)"/><path d="M1 2l8 6 8-6" stroke="#1d1f1c" stroke-width="1.6" fill="none"/></svg><span>hello@brookvaleyardworks.com</span></div>

  <div class="abs" style="left:0;top:228px;width:1200px;height:1px;background:#3a3d38"></div>
  <p class="abs center" style="left:0;top:262px;width:1200px;font-size:15px;color:#e6e6e6"><b style="color:var(--lime)">OFFICE HOURS :</b> Mon - Thurs : 8am to 5pm &nbsp;|&nbsp; Fri : 8am to 3pm &nbsp;|&nbsp; Sat-Sun : Closed</p>
  <p class="abs center" style="left:0;top:296px;width:1200px;font-size:13px;color:#9a9a9a">© Copyright 2019 &nbsp;|&nbsp; All Rights Reserved &nbsp;|&nbsp; Terms &amp; Condition &nbsp;|&nbsp; Privacy Policy</p>
</footer>

</body>
</html>
```